Quolvex custom business card design

Need a authentic, innovative business card design for a new mobile app business. I am uploading a few screen images from our app for you to view. I would like app design theme to match business card design. I can also send logo images.

```html
<!DOCTYPE html>
<html lang="en">
<head>
<meta charset="utf-8">
<title>Quolvex business card</title>
<link rel="stylesheet" href="https://fonts.googleapis.com/css2?family=Mulish:wght@400;800&display=swap">
<style>
  :root {
    --purple: #6a2e9a;
    --purple-light: #8d5cbb;
    --ink: #262626;
    --paper: #ffffff;
    --backdrop: #ece9ef;
    --rule: #3a3a3a;
  }
  * { margin: 0; padding: 0; box-sizing: border-box; }
  html, body { width: 1200px; height: 831px; overflow: hidden; }
  body {
    background: var(--backdrop);
    font-family: "Mulish", Arial, sans-serif;
    position: relative;
  }
  .card {
    position: absolute;
    left: 280px;
    width: 640px;
    height: 366px;
    overflow: hidden;
    box-shadow: 0 6px 20px rgba(0,0,0,.18);
  }
  .card-front { top: 30px; background: var(--purple); }
  .card-back  { top: 436px; background: var(--paper); }

  /* front */
  .front-brand {
    position: absolute;
    left: 0; right: 0; top: 150px;
    display: flex; align-items: center; justify-content: center; gap: 16px;
  }
  .front-brand .dot {
    width: 40px; height: 40px; border-radius: 50%;
    background: var(--purple-light);
  }
  .front-brand .name {
    font-weight: 800; font-size: 52px; color: var(--purple-light);
    letter-spacing: 1px;
  }

  /* back */
  .back-brand {
    position: absolute; left: 70px; top: 118px;
    display: flex; align-items: center; gap: 12px;
  }
  .back-brand .dot {
    width: 30px; height: 30px; border-radius: 50%; background: var(--purple);
  }
  .back-brand .name {
    font-weight: 800; font-size: 40px; color: var(--ink);
  }
  .divider {
    position: absolute; left: 335px; top: 70px;
    width: 1.5px; height: 180px; background: var(--rule);
  }
  .person { position: absolute; left: 365px; top: 88px; }
  .person .full-name {
    font-weight: 800; font-size: 28px; color: var(--purple); line-height: 1.1;
  }
  .person .title { font-size: 18px; color: var(--ink); margin-top: 2px; }
  .contacts { position: absolute; left: 365px; top: 170px; list-style: none; }
  .contacts li {
    display: flex; align-items: center; gap: 10px;
    font-size: 19px; color: var(--ink); line-height: 27px;
  }
  .contacts svg { width: 16px; height: 16px; fill: var(--purple); flex: none; }
  .band-address {
    position: absolute; left: 0; top: 300px; width: 360px; height: 32px;
    background: var(--purple); color: var(--paper);
    font-size: 16px; line-height: 32px; padding-left: 22px;
  }
  .band-dark {
    position: absolute; left: 360px; top: 300px; right: 0; height: 32px;
    background: var(--ink);
  }
  .band-knob { position: absolute; left: 350px; top: 300px; width: 26px; height: 32px; }
</style>
</head>
<body>
  <section class="card card-front" aria-label="Card front">
    <div class="front-brand">
      <span class="dot"></span>
      <span class="name">Quolvex</span>
    </div>
  </section>

  <section class="card card-back" aria-label="Card back">
    <div class="back-brand">
      <span class="dot"></span>
      <span class="name">Quolvex</span>
    </div>
    <div class="divider"></div>
    <div class="person">
      <div class="full-name">Your Name</div>
      <div class="title">Your Title</div>
    </div>
    <ul class="contacts">
      <li>
        <svg viewBox="0 0 24 24"><path d="M6.6 10.8a15.1 15.1 0 0 0 6.6 6.6l2.2-2.2a1 1 0 0 1 1-.25 11.4 11.4 0 0 0 3.6.57 1 1 0 0 1 1 1V20a1 1 0 0 1-1 1A17 17 0 0 1 3 4a1 1 0 0 1 1-1h3.5a1 1 0 0 1 1 1c0 1.25.2 2.45.57 3.57a1 1 0 0 1-.25 1z"/></svg>
        123-456-2100
      </li>
      <li>
        <svg viewBox="0 0 24 24"><path d="M2 5h20v14H2z M2 5l10 8 10-8" /></svg>
        youremail@example.com
      </li>
      <li>
        <svg viewBox="0 0 24 24"><circle cx="12" cy="12" r="10"/><path d="M2 12h20M12 2c3 3 3 17 0 20M12 2c-3 3-3 17 0 20" stroke="#fff" stroke-width="1.5" fill="none"/></svg>
        www.yourwebsite.com
      </li>
    </ul>
    <div class="band-address">Your address, city, state, ZIP 0000</div>
    <div class="band-dark"></div>
    <svg class="band-knob" viewBox="0 0 26 32" aria-hidden="true">
      <path d="M10 7 A9 9 0 0 1 10 25" fill="var(--purple)" stroke="#fff" stroke-width="2.5"/>
      <rect x="0" y="0" width="10" height="32" fill="var(--purple)"/>
    </svg>
  </section>
</body>
</html>
```